Alloy wheel repair business needs a website

Install logo previously purchased from pixelbazaar, toolbar with dropdowns. services, gallery, clients , contact ect
Maybe mission statment

Target Market(s)

vehicle owners, auto dealers,insurance companies,

Industry/Entity Type

Alloy Wheel Repair

Coding

Coded - Design and coding required

Number of Pages Required

4 page

Font styles to use
Sans Serif

Colors
0054AA
0677BA
7BADD7
CADEEF
E8F1F8

```html
<!DOCTYPE html>
<html lang="en">
<head>
<meta charset="utf-8">
<title>Rimcraft Wheel Works – Alloy Wheel Repair</title>
<link rel="stylesheet" href="https://fonts.googleapis.com/css2?family=Jost:wght@400;500;600&family=Orbitron:wght@800;900&family=Kaushan+Script&family=Josefin+Sans:wght@400;600&display=swap">
<style>
:root{
  --blue:#3a86c8;
  --blue-deep:#0054aa;
  --blue-mid:#0677ba;
  --blue-soft:#7badd7;
  --blue-pale:#cadeef;
  --blue-mist:#e8f1f8;
  --ink:#111;
  --header:#2b2e33;
  --grey-bg:#efefef;
  --text:#555;
  --white:#fff;
  --black:#050505;
  --body:"Jost",sans-serif;
  --display:"Orbitron",sans-serif;
}
*{box-sizing:border-box;margin:0;padding:0}
html,body{width:1200px;height:4769px;overflow:hidden}
body{position:relative;background:var(--white);font-family:var(--body);color:var(--text)}
.abs{position:absolute}
.photo{position:absolute}

/* top bar */
.topbar{position:absolute;left:0;top:0;width:1200px;height:28px;background:var(--blue);color:var(--white);font-size:10px}
.topbar .contact{position:absolute;left:66px;top:8px;display:flex;gap:16px;align-items:center}
.topbar .tag{position:absolute;left:0;right:0;top:8px;text-align:center;font-weight:600;letter-spacing:.3px}
.topbar .socials{position:absolute;right:0;top:0;display:flex}
.topbar .socials span{width:26px;height:28px;border-left:1px solid rgba(255,255,255,.35);display:flex;align-items:center;justify-content:center}
.topbar .socials i{width:10px;height:10px;border-radius:50%;background:var(--white);display:block}

/* header */
.header{position:absolute;left:0;top:28px;width:1200px;height:100px;background:var(--header)}
.brand{position:absolute;display:flex;align-items:center;gap:8px;font-family:var(--body);font-weight:600;color:var(--blue)}
.header .brand{left:61px;top:34px;font-size:21px}
.brand .dot{width:16px;height:16px;border-radius:50%;background:var(--blue)}
.nav{position:absolute;left:282px;top:43px;display:flex;gap:29px;color:var(--white);font-size:13px}
.nav-cta{position:absolute;left:1024px;top:34px;width:107px;height:34px;border:1px solid var(--blue);color:var(--blue);font-size:11px;display:flex;align-items:center;justify-content:center}

/* hero */
.hero{position:absolute;left:0;top:128px;width:1200px;height:494px;background:linear-gradient(90deg,#26303a 0%,#3b4650 45%,#1a1d21 75%,#0d0f11 100%)}
.hero .welcome{position:absolute;left:59px;top:52px;font-family:"Kaushan Script",cursive;font-size:34px;color:var(--white)}
.hero h1{position:absolute;left:59px;top:104px;font-family:var(--display);font-weight:900;font-style:italic;font-size:50px;line-height:61px;color:var(--white);letter-spacing:1px}
.hero h1 em{color:var(--blue);font-style:italic}
.hero p{position:absolute;left:59px;top:300px;font-size:12px;color:var(--white)}
.btn{position:absolute;background:var(--blue);color:var(--white);font-size:14px;font-weight:500;display:flex;align-items:center;justify-content:center;letter-spacing:.5px}

/* headings */
.title{font-family:var(--display);font-weight:900;font-style:italic;color:var(--ink);font-size:38px;line-height:46px;letter-spacing:1.5px}
.title em{color:var(--blue);font-style:italic}
.rule{position:absolute;height:2px;display:flex;gap:6px}
.rule i{display:block;height:2px;background:var(--blue-soft);flex:1}

/* details */
.details-title{position:absolute;left:163px;top:710px}
.details-copy{position:absolute;left:706px;top:716px;width:352px;font-size:13px;line-height:24px}

/* services */
.services{position:absolute;left:0;top:1426px;width:1200px;height:754px;background:var(--grey-bg)}
.center{position:absolute;left:0;width:1200px;text-align:center}
.tile{position:absolute;width:273px;height:239px;overflow:hidden}
.tile .label{position:absolute;left:0;bottom:0;width:100%;height:41px;background:var(--blue);color:var(--white);font-size:14px;font-weight:500;display:flex;align-items:center;justify-content:center;letter-spacing:.5px}
.tile.feature{background:#0e1a2b;color:var(--white);text-align:center}
.tile.feature h3{margin-top:32px;font-size:15px;font-weight:500;letter-spacing:.5px}
.tile.feature p{margin:14px auto 0;width:200px;font-size:10px;line-height:22px}
.tile.feature .more{position:absolute;left:62px;top:184px;width:148px;height:32px;border:1px solid #ccc;font-size:10px;display:flex;align-items:center;justify-content:center}

/* stats */
.stats{position:absolute;left:17px;top:3011px;width:1168px;height:198px;background:var(--blue)}
.stat{position:absolute;top:50px;width:240px;text-align:center;color:var(--white)}
.stat b{display:block;font-family:var(--display);font-weight:900;font-size:58px;line-height:66px}
.stat span{display:block;font-family:var(--display);font-weight:800;font-style:italic;font-size:11px;letter-spacing:1px}
.stats .divider{position:absolute;top:45px;width:1px;height:110px;background:rgba(255,255,255,.35)}

/* reviews */
.review{position:absolute;background:var(--white);box-shadow:0 4px 18px rgba(0,0,0,.12);text-align:center;font-size:11px;line-height:24px}
.review .q{font-family:Georgia,serif;font-size:36px;color:var(--blue);line-height:36px;font-weight:700}
.review p{margin:10px auto 0;width:270px}
.review .who{margin-top:14px;font-family:"Josefin Sans",sans-serif;font-size:12px;color:var(--blue)}
.review.active{background:var(--blue);color:var(--white);box-shadow:none;outline:2px solid var(--blue);border:2px solid rgba(255,255,255,.6)}
.review.active .q,.review.active .who{color:var(--white)}

/* quote form */
.form-card{position:absolute;left:146px;top:3782px;width:385px;height:407px;background:var(--white);box-shadow:0 4px 20px rgba(0,0,0,.12)}
.form-card h2{position:absolute;left:36px;top:50px;font-family:var(--display);font-weight:900;font-style:italic;font-size:17px;color:var(--ink);letter-spacing:1px}
.field{position:absolute;left:32px;width:322px;height:35px;border:1px solid #e2e2e2;font-size:10px;color:#b5b5b5;padding:10px 12px;letter-spacing:.5px}
.field.focus{border:2px solid var(--blue)}

/* footer */
.footer{position:absolute;left:0;top:4263px;width:1200px;height:506px;background:var(--black);clip-path:polygon(0 0,62% 0,68% 70px,100% 70px,100% 100%,0 100%);color:var(--white)}
.footer h4{position:absolute;font-size:22px;font-weight:500}
.footer .links{position:absolute;left:430px;top:182px;font-size:12px;line-height:30.5px}
.footer .about{position:absolute;left:169px;top:226px;width:200px;font-size:12px;line-height:22px}
.footer .social{position:absolute;top:303px;width:34px;height:34px;border-radius:50%;border:1px solid #fff}
.footer .social.on{background:var(--blue);border-color:var(--blue)}
.footer .line{position:absolute;left:0;top:432px;width:1200px;height:1px;background:#222}
.footer .copy{position:absolute;left:0;top:452px;width:1200px;text-align:center;font-size:11px}
</style>
</head>
<body>

<div class="topbar">
  <div class="contact">
    <span>&#9990; 555-014-2291</span>
    <span>|</span>
    <span>&#9993; hello@rimcraftwheels.com</span>
  </div>
  <div class="tag">RIMCRAFT WHEEL REPAIR SERVICES</div>
  <div class="socials"><span><i></i></span><span><i></i></span><span><i></i></span><span><i></i></span></div>
</div>

<header class="header">
  <div class="brand"><span class="dot"></span>RIMCRAFT</div>
  <nav class="nav">
    <span>Wheel Repair Services</span><span>Wheel Custom Coloring</span><span>Company</span><span>Wheel Repair Gallery</span><span>Find a Location</span><span>Blog</span>
  </nav>
  <div class="nav-cta">CONTACT US</div>
</header>

<section class="hero" role="img" aria-label="Workshop photo: alloy wheel mounted on a tyre machine with a mechanic in the background">
  <div class="welcome">Welcome To The</div>
  <h1><em>ALLOY</em> WHEEL<br>REPAIR<br>SERVICES</h1>
  <p>Lorem ipsum dolor sit amet, consectetur adipiscing elit, sed do</p>
  <div class="btn" style="left:59px;top:352px;width:145px;height:44px;">CONTACT US</div>
</section>

<!-- details -->
<h2 class="title details-title">WE KNOW THE<br><em>DIFFERENCE</em><br>IS IN THE <em>DETAILS.</em></h2>
<div class="rule" style="left:163px;top:866px;width:124px"><i></i><i></i><i></i></div>
<p class="details-copy">Lorem ipsum dolor sit amet, consectetur adipiscing elit, sed do eiusmod tempor incididunt ut labore et dolore magna aliqua. Quis ipsum suspendisse ultrices gravida.</p>
<div class="btn" style="left:707px;top:822px;width:147px;height:43px;">LEARN MORE</div>
<div class="photo" style="left:422px;top:902px;width:635px;height:363px;background:linear-gradient(135deg,#8a96a3,#4a5561 55%,#2b3138)" role="img" aria-label="Technician fitting a tyre onto an alloy rim with a tyre lever"></div>
<div class="photo" style="left:152px;top:996px;width:384px;height:356px;background:var(--white)"></div>
<div class="photo" style="left:161px;top:1006px;width:365px;height:337px;background:linear-gradient(160deg,#6b7077,#3a3e44 60%,#26292d)" role="img" aria-label="Mechanic inspecting a tyre with a torch"></div>

<!-- services -->
<section class="services">
  <h2 class="title center" style="top:50px">ALLAY WHEEL REPAIR<br><em>SERVICES</em></h2>
  <div class="rule" style="left:538px;top:157px;width:124px"><i></i><i></i><i></i></div>

  <div class="tile feature" style="left:139px;top:196px">
    <h3>WHEEL REPAIR SERVICES</h3>
    <p>We fix wheel &amp; rim damage such as scratched and/or bent alloy wheels and minor cracks. We can return many wheels to like-new.</p>
    <div class="more">READ US MORE</div>
  </div>
  <div class="tile" style="left:433px;top:196px;background:linear-gradient(160deg,#a33,#555 45%,#2a2a2a)" role="img" aria-label="Wheel on a refinishing lathe"><div class="label">WHEEL REFINISHING</div></div>
  <div class="tile" style="left:728px;top:196px;background:linear-gradient(180deg,#6d625a,#2a2a2a)" role="img" aria-label="Rows of new tyres"><div class="label">WHEEL REMANUFACTURING</div></div>
  <div class="tile" style="left:139px;top:454px;background:linear-gradient(160deg,#d8d8d8,#444 60%,#1c1c1c)" role="img" aria-label="Black painted alloy rim being sprayed"><div class="label">WHEEL CUSTOM COLORING</div></div>
  <div class="tile" style="left:433px;top:454px;background:linear-gradient(160deg,#777,#3b3b3b 60%,#222)" role="img" aria-label="Wheel on a balancing machine"><div class="label">WHEEL REFURB</div></div>
  <div class="tile" style="left:728px;top:454px;background:linear-gradient(160deg,#b8bcc0,#555 55%,#2e3236)" role="img" aria-label="Mechanic straightening an alloy wheel"><div class="label">WHEEL STRAIGHTENING</div></div>
</section>

<!-- gallery -->
<h2 class="title center" style="top:2251px">WHEEL REPAIR<br>GARAGE <em>GALLERY</em></h2>
<div class="rule" style="left:538px;top:2355px;width:124px"><i></i><i></i><i></i></div>
<div role="img" aria-label="Gallery of garage photos: mechanics fitting tyres, tyre stacks and wheel service">
  <div class="photo" style="left:0;top:2424px;width:161px;height:289px;background:linear-gradient(160deg,#666,#333)"></div>
  <div class="photo" style="left:0;top:2722px;width:161px;height:211px;background:linear-gradient(160deg,#8c8c8c,#3a3a3a)"></div>
  <div class="photo" style="left:165px;top:2415px;width:289px;height:292px;background:linear-gradient(160deg,#9aa0a6,#4a4a4a 55%,#6b4a3a)"></div>
  <div class="photo" style="left:165px;top:2722px;width:289px;height:211px;background:linear-gradient(160deg,#dde3e8,#6a6f74)"></div>
  <div class="photo" style="left:459px;top:2465px;width:291px;height:296px;background:linear-gradient(180deg,#e8ecef,#2f6a4a 40%,#2a2a2a)"></div>
  <div class="photo" style="left:459px;top:2772px;width:291px;height:161px;background:linear-gradient(160deg,#f0f0f0,#3b5fa8 60%,#777)"></div>
  <div class="photo" style="left:754px;top:2393px;width:289px;height:294px;background:linear-gradient(180deg,#3a3f45,#cfd4d8 60%,#2a4f9a)"></div>
  <div class="photo" style="left:754px;top:2702px;width:289px;height:231px;background:linear-gradient(160deg,#2d5fb0,#c98a2e 55%,#2a2a2a)"></div>
  <div class="photo" style="left:1048px;top:2483px;width:152px;height:289px;background:linear-gradient(180deg,#cfcfcf,#2a2a2a)"></div>
  <div class="photo" style="left:1048px;top:2783px;width:152px;height:150px;background:linear-gradient(160deg,#bbb,#333)"></div>
</div>

<!-- stats -->
<section class="stats">
  <div class="stat" style="left:109px"><b>25120</b><span>WHEELS REFURBISHED</span></div>
  <div class="divider" style="left:348px"></div>
  <div class="stat" style="left:365px"><b>2548</b><span>WHEELS STRAIGHTENED</span></div>
  <div class="divider" style="left:608px"></div>
  <div class="stat" style="left:609px"><b>8367</b><span>DIAMOND POLISHED</span></div>
  <div class="divider" style="left:850px"></div>
  <div class="stat" style="left:844px"><b>2248</b><span>WELDED</span></div>
</section>

<!-- reviews -->
<h2 class="title center" style="top:3292px">CLIENT <em>REVIEWS</em></h2>
<div class="rule" style="left:538px;top:3351px;width:124px"><i></i><i></i><i></i></div>
<div class="review" style="left:63px;top:3413px;width:367px;height:222px;padding-top:34px">
  <div class="q">&ldquo;</div>
  <p>Lorem ipsum dolor sit amet, consectetur adipisicing elit, sed do eiusmod tempor incididunt ut labore et dolore magna aliqua. Ut enim ad minim veniam, quis nostrud exercitation ullam-</p>
  <div class="who">MARK D.</div>
</div>
<div class="review active" style="left:437px;top:3398px;width:324px;height:254px;padding-top:36px">
  <div class="q">&ldquo;</div>
  <p>Lorem ipsum dolor sit amet, consectetur adipisicing elit, sed do eiusmod tempor incididunt ut labore et dolore magna aliqua. Ut enim ad minim veniam, quis nostrud exercitation ullamco laboris</p>
  <div class="who">TINA R.</div>
</div>
<div class="review" style="left:767px;top:3413px;width:370px;height:222px;padding-top:34px">
  <div class="q">&ldquo;</div>
  <p>Lorem ipsum dolor sit amet, consectetur adipisicing elit, sed do eiusmod tempor incididunt ut labore et dolore magna aliqua. Ut enim ad minim veniam, quis nostrud exercitation ullamco</p>
  <div class="who" style="color:#222">OLIVIA K.</div>
</div>

<!-- quote form -->
<div class="photo" style="left:0;top:3850px;width:1200px;height:483px;background:linear-gradient(180deg,#fff 0%,#e4e6e8 30%,#9a9da1 70%,#5d6064 100%)" role="img" aria-label="Dark blue convertible luxury car on an open road"></div>
<div class="photo" style="left:500px;top:3900px;width:680px;height:330px;background:radial-gradient(ellipse at 60% 55%,#0f1a2e 0%,#1b2436 45%,rgba(27,36,54,0) 72%)"></div>
<div class="form-card">
  <h2>READY FOR THE NEXT</h2>
  <div class="field focus" style="top:89px">FIRST NAME</div>
  <div class="field" style="top:144px">LAST NAME</div>
  <div class="field" style="top:196px">EMAIL ADDRESS</div>
  <div class="field" style="top:242px;height:69px">PHONE NUMBER</div>
  <div class="btn" style="left:47px;top:335px;width:164px;height:41px;">SUBMIT NOW</div>
</div>

<!-- footer -->
<footer class="footer">
  <div class="brand" style="left:169px;top:138px;font-size:20px"><span class="dot"></span>RIMCRAFT</div>
  <p class="about">Lorem ipsum dolor sit amet, consectetur adipiscing elit, sed do eiusmod tempor</p>
  <span class="social on" style="left:168px"></span>
  <span class="social" style="left:218px"></span>
  <span class="social" style="left:266px"></span>
  <span class="social" style="left:316px"></span>

  <h4 style="left:428px;top:130px">Quick Links</h4>
  <div class="links">Wheel Repair Services<br>Wheel Custom Coloring<br>Company<br>Wheel Repair<br>Gallery<br>Find a Locatio<br>Blog</div>

  <h4 style="left:604px;top:130px">Contact Us</h4>
  <div class="abs" style="left:606px;top:183px;font-size:12px;line-height:30px">&#9993;&nbsp; hello@rimcraftwheels.com<br>&#9990;&nbsp; 555-014-2291</div>

  <h4 style="left:811px;top:130px">Newsletter</h4>
  <p class="abs" style="left:813px;top:178px;width:245px;font-size:11.5px;line-height:15px">Sign up to our newsletter to receive the latest news and special discounts.</p>
  <div class="abs" style="left:813px;top:224px;width:174px;height:35px;background:var(--white);color:#aaa;font-size:9px;padding:12px 16px">Email Address...</div>
  <div class="abs" style="left:987px;top:224px;width:45px;height:35px;background:var(--blue)">
    <svg width="45" height="35" viewBox="0 0 45 35"><path d="M14 18 L32 10 L27 27 L22 21 Z" fill="#fff"/></svg>
  </div>

  <div class="line"></div>
  <div class="copy">&copy; Copyright 2023 Rimcraft Wheel Works. All Rights Reserved.</div>
</footer>

</body>
</html>
```